Word document template for sales proposals

I am after a template that is simple but impactful. Use of colour to be limited but some for impact would be good. The proposals are for use in the professional technical field.

```html
<!DOCTYPE html>
<html lang="en">
<head>
<meta charset="utf-8">
<title>Voltline Proposal Letterhead</title>
<link href="https://fonts.googleapis.com/css2?family=Poppins:wght@400;500;600;700&display=swap" rel="stylesheet">
<style>
  :root {
    --brand-blue: #2a9fd8;
    --brand-blue-deep: #1f82c0;
    --brand-orange: #f5a31a;
    --ink: #333842;
    --ink-soft: #5b616b;
    --paper: #ffffff;
    --signature-tone: #d9dde3;
  }
  * { margin: 0; padding: 0; box-sizing: border-box; }
  html, body {
    width: 849px;
    height: 1200px;
    overflow: hidden;
    background: var(--paper);
  }
  .letterhead {
    position: relative;
    width: 849px;
    height: 1200px;
    background: var(--paper);
    font-family: "Poppins", sans-serif;
    color: var(--ink);
    overflow: hidden;
  }
  .accent-band {
    position: absolute;
    left: 0;
    width: 849px;
  }
  .accent-band--top {
    top: 0;
    height: 22px;
    background: linear-gradient(90deg, var(--brand-blue) 0%, var(--brand-blue) 55%, var(--brand-orange) 100%);
  }
  .accent-band--bottom {
    bottom: 0;
    height: 96px;
    background: linear-gradient(180deg, var(--brand-orange) 0%, var(--brand-blue) 55%, var(--brand-blue-deep) 100%);
  }

  .brand {
    position: absolute;
    top: 52px;
    left: 70px;
    display: flex;
    align-items: center;
    gap: 12px;
  }
  .brand__dot {
    width: 38px; height: 38px;
    border-radius: 50%;
    background: var(--brand-orange);
  }
  .brand__name {
    font-weight: 700;
    font-size: 26px;
    letter-spacing: 1px;
    color: var(--brand-blue);
  }

  .recipient {
    position: absolute;
    top: 170px;
    left: 70px;
    font-size: 12px;
    line-height: 1.6;
  }
  .recipient__label { color: var(--ink-soft); margin-bottom: 8px; }
  .recipient__name { font-weight: 600; }
  .recipient__role { font-weight: 500; }

  .letter-date {
    position: absolute;
    top: 262px;
    right: 70px;
    font-size: 12px;
    font-weight: 500;
  }
  .salutation {
    position: absolute;
    top: 262px;
    left: 70px;
    font-size: 13px;
    font-weight: 600;
  }

  .letter-body {
    position: absolute;
    top: 320px;
    left: 70px;
    width: 709px;
    font-size: 13px;
    line-height: 1.75;
    color: var(--ink-soft);
  }
  .letter-body p + p { margin-top: 20px; }

  .sign-off {
    position: absolute;
    top: 680px;
    left: 70px;
    font-size: 12px;
  }
  .sign-off__regards { color: var(--ink-soft); }
  .sign-off__signature {
    width: 170px;
    height: 54px;
    margin: 8px 0 6px;
    border-radius: 4px;
    background: linear-gradient(90deg, var(--signature-tone), #eef0f3);
  }
  .sign-off__name { font-weight: 600; font-size: 13px; }
  .sign-off__role { color: var(--ink-soft); }
</style>
</head>
<body>
<main class="letterhead">
  <div class="accent-band accent-band--top" role="img" aria-label="Decorative orange and blue header band"></div>

  <div class="brand">
    <span class="brand__dot"></span>
    <span class="brand__name">VOLTLINE</span>
  </div>

  <section class="recipient">
    <p class="recipient__label">To</p>
    <p class="recipient__name">Adrian Kolby</p>
    <p class="recipient__role">Northgate Systems / CEO</p>
    <p>48 Harbour Lane, Westfield, ST 20418</p>
  </section>

  <p class="salutation">Dear Mr. Adrian Kolby</p>
  <p class="letter-date">Oct 16, 2022</p>

  <section class="letter-body">
    <p>Thank you for the opportunity to present this proposal for your upcoming project. Our team has reviewed your requirements in detail and prepared a clear plan covering scope, schedule and cost. We believe our technical experience will help you reach your goals on time and within budget.</p>
    <p>This document outlines the services we propose, the methods we will use and the results you can expect. Each stage is described with its deliverables, so your team can follow progress and review work at every step.</p>
    <p>Our pricing is set out in the attached schedule and remains valid for thirty days. All figures include labour, materials and on-site support, with no hidden costs added later.</p>
    <p>Please contact us with any questions. We look forward to working with you and to building a lasting partnership.</p>
  </section>

  <section class="sign-off">
    <p class="sign-off__regards">Regards,</p>
    <div class="sign-off__signature" role="img" aria-label="Handwritten signature of the sender"></div>
    <p class="sign-off__name">Marlene Oduya</p>
    <p class="sign-off__role">General Manager</p>
  </section>

  <div class="accent-band accent-band--bottom" role="img" aria-label="Decorative orange and blue footer band"></div>
</main>
</body>
</html>
```